Hearthside Pots: A Patient Palate's Companion

Hi, I had a book cover designed on this site, but I want to modify the cover and change the colours. I want to keep the slow cooker and the ingredients on the cover, but I want to simplify it a bit. And, I am open to other ideas. I have attached below a book cover idea I like and I like the colors as well. I want it to be called Hearthside Pots, with the language on the right corner: "Curated For Nearly Effortless Meals That Are Greater Than The Sum Of Their Ingredients" I like the circles idea and my name as the author on the curve.

Target Market(s)

Home Cooks

Colors
00AB8E
00BBA5
67D7C9
C6EFE9
E9F9F6
F0912C
F2A743
F7CA91
FBE8D2
FDF5EE
E54698
E96AAD
F1A4CE
F9D9EA
FCEFF6
6B429C
8869AF
B7A5CE
E3DAEB
F3F0F8

Requirements
Must have
• Please use the colors on the Marigold Table Recipe Book and I like the design, but I do not want it identical. I like the author name (Harold P. Quimby) on the side of the circle on the upper right side of the cover.
Nice to have
• I like the large words "Hearthside Pots"

```html
<!DOCTYPE html>
<html lang="en">
<head>
<meta charset="utf-8">
<title>Hearthside Pots – Book Cover</title>
<link href="https://fonts.googleapis.com/css2?family=Cinzel:wght@400;600;700&display=swap" rel="stylesheet">
<style>
  :root{
    --stage:#2bd1c5;
    --cover-green:#0e9a86;
    --cover-green-deep:#0a7f70;
    --night:#3a3456;
    --olive:#8f7f4e;
    --orange:#c8683a;
    --teal:#3f8a8a;
    --violet:#6b429c;
    --gold-light:#f6d27a;
    --gold:#e3a93a;
    --gold-dark:#b9781c;
    --ink-light:#fdf5ee;
  }
  *{margin:0;padding:0;box-sizing:border-box}
  html,body{width:1139px;height:1200px;overflow:hidden;background:var(--stage)}
  .canvas{position:relative;width:1139px;height:1200px}
  .cover{
    position:absolute;left:190px;top:45px;width:760px;height:1110px;
    background:linear-gradient(160deg,var(--cover-green) 0%,var(--cover-green-deep) 100%);
    overflow:hidden;
  }
  .artwork{
    position:absolute;left:40px;top:60px;width:1120px;height:1120px;border-radius:50%;
    background:
      radial-gradient(circle at 38% 30%,rgba(200,104,58,.75) 0%,rgba(200,104,58,0) 40%),
      radial-gradient(circle at 20% 60%,rgba(63,138,138,.6) 0%,rgba(63,138,138,0) 35%),
      radial-gradient(circle at 25% 85%,rgba(107,66,156,.6) 0%,rgba(107,66,156,0) 35%),
      linear-gradient(180deg,var(--night) 0%,#4a3d55 50%,#2f4a5a 100%);
  }
  .author-art{position:absolute;inset:0;width:760px;height:1110px}
  .author{font-family:'Cinzel',serif;font-size:22px;letter-spacing:4px;fill:var(--ink-light)}
  .title{
    position:absolute;left:110px;top:520px;
    font-family:'Cinzel',serif;font-weight:700;line-height:1.08;
    transform:rotate(-15deg);transform-origin:left top;
    background:linear-gradient(180deg,var(--gold-light),var(--gold) 55%,var(--gold-dark));
    -webkit-background-clip:text;background-clip:text;color:transparent;
  }
  .title-line{display:block;font-size:74px}
  .title-line--second{padding-left:150px}
  .tagline{
    position:absolute;left:390px;top:690px;width:330px;
    transform:rotate(-12deg);transform-origin:center;
    font-family:'Cinzel',serif;font-size:19px;line-height:1.3;letter-spacing:1px;
    text-transform:uppercase;color:var(--ink-light);text-align:center;
  }
  .tagline-rule{position:relative;display:block;margin:14px auto 0;width:240px;height:2px;background:var(--gold)}
  .tagline-rule::after{
    content:"";position:absolute;left:50%;top:-4px;width:8px;height:8px;margin-left:-4px;
    background:var(--gold);transform:rotate(45deg);
  }
  .photo{position:absolute}
  .photo--ingredients{
    left:40px;top:860px;width:400px;height:220px;border-radius:45%;
    background:radial-gradient(ellipse at 45% 50%,#c8543a 0%,#7f8f4a 45%,rgba(122,70,173,0) 75%);
  }
  .photo--pot{
    left:450px;top:890px;width:280px;height:200px;border-radius:48%;
    background:radial-gradient(ellipse at 50% 55%,#e59a40 0%,#4f7a3a 45%,#1e1e1e 68%,rgba(30,30,30,0) 78%);
  }
</style>
</head>
<body>
<main class="canvas">
  <section class="cover" aria-label="Hearthside Pots book cover">
    <div class="artwork" role="img" aria-label="Large dark circle filled with soft overlapping textured colour circles in olive, rust, orange, teal, red and violet"></div>

    <svg class="author-art" viewBox="0 0 760 1110" aria-hidden="true">
      <defs>
        <path id="author-arc" d="M 50 420 A 585 585 0 0 1 353 90"/>
      </defs>
      <text class="author"><textPath href="#author-arc">HAROLD P. QUIMBY</textPath></text>
    </svg>

    <h1 class="title">
      <span class="title-line">Hearthside</span>
      <span class="title-line title-line--second">Pots</span>
    </h1>

    <p class="tagline">Curated for nearly effortless meals that are greater than the sum of their ingredients.<span class="tagline-rule"></span></p>

    <div class="photo photo--ingredients" role="img" aria-label="Fresh vegetables tumbling: tomatoes, peppers, onions, zucchini and lettuce"></div>
    <div class="photo photo--pot" role="img" aria-label="Black cooking pot with lifted glass lid, filled with carrots, peppers and herbs"></div>
  </section>
</main>
</body>
</html>
```